Tolvek Marketing Consulting business card

I have a new logo that was designed for me here on PixelHarbor. I am a medical device marketing consultant. The medical device industry is very professional, kind of dry, and can be a bit boring. But I'm in marketing so I want to look fresh and innovative, within the confines of the industry.

Please use the logo to its potential, making it colorful and visually interesting (I know, there's really only one color. I need some kind of interesting design element - maybe wraparound...

Target Market(s)

Marketing management in medical device companies.

Industry/Entity Type

Marketing

Requirements
Must have
• Marisol Tolvek
Phone: 949-218-4073
Address: Harbor Cove, CA
marisol@tolvekmarketingconsulting.example
www.tolvekmarketingconsulting.example

```html
<!DOCTYPE html>
<html lang="en">
<head>
<meta charset="utf-8">
<title>Tolvek Marketing Consulting — Business Card</title>
<link rel="stylesheet" href="https://fonts.googleapis.com/css2?family=Open+Sans:wght@400;600&display=swap">
<style>
  :root {
    --backdrop: #e9e7e3;
    --card-white: #ffffff;
    --card-black: #1c1c1d;
    --brand-blue: #1f9ae0;
    --ink-grey: #5a5a5c;
    --ink-light: #f2f2f2;
    --shadow: rgba(0, 0, 0, 0.22);
  }
  * { box-sizing: border-box; margin: 0; padding: 0; }
  html, body {
    width: 1200px; height: 1024px; overflow: hidden;
    background: var(--backdrop);
    font-family: "Open Sans", Arial, sans-serif;
  }
  .canvas { position: relative; width: 1200px; height: 1024px; }
  .card {
    position: absolute; left: 250px; width: 700px; height: 400px;
    box-shadow: 0 10px 28px var(--shadow);
    overflow: hidden;
  }
  .card--front { top: 80px; background: var(--card-white); }
  .card--back { top: 544px; background: var(--card-black); }

  /* front */
  .divider {
    position: absolute; left: 0; right: 0; top: 214px;
    height: 2px; background: var(--brand-blue);
  }
  .wordmark {
    position: absolute; font-weight: 600; color: var(--brand-blue);
    line-height: 1.05; white-space: nowrap;
  }
  .card--front .wordmark { left: 48px; top: 108px; font-size: 38px; }
  .wordmark__sub {
    display: block; font-size: 0.42em; letter-spacing: 0.42em; margin-top: 6px;
    text-transform: uppercase;
  }
  .holder-name {
    position: absolute; right: 48px; top: 176px;
    font-size: 22px; color: var(--ink-grey); font-weight: 400; white-space: nowrap;
  }
  .contact-list { position: absolute; list-style: none; font-size: 15px; color: var(--ink-grey); }
  .contact-list li { display: flex; align-items: center; gap: 10px; margin-bottom: 12px; white-space: nowrap; }
  .contact-list svg { width: 16px; height: 16px; flex: none; fill: var(--brand-blue); }
  .contact-list--left { left: 48px; top: 262px; }
  .contact-list--right { right: 48px; top: 262px; font-size: 13.5px; }

  /* back */
  .web-address {
    position: absolute; left: 0; right: 0; top: 110px; text-align: center;
    font-size: 12px; letter-spacing: 0.3em; color: var(--ink-light);
    text-transform: uppercase; white-space: nowrap;
  }
  .card--back .wordmark {
    left: 0; right: 0; top: 150px; text-align: center;
    font-size: 46px; color: var(--ink-light);
  }
</style>
</head>
<body>
<main class="canvas">
  <section class="card card--front" aria-label="Card front">
    <div class="divider"></div>
    <p class="wordmark">Tolvek Marketing<span class="wordmark__sub">Consulting</span></p>
    <p class="holder-name">Marisol Tolvek</p>
    <ul class="contact-list contact-list--left">
      <li>
        <svg viewBox="0 0 16 16" aria-hidden="true"><path d="M8 0a5.5 5.5 0 0 0-5.5 5.5C2.5 10 8 16 8 16s5.5-6 5.5-10.5A5.5 5.5 0 0 0 8 0zm0 8a2.5 2.5 0 1 1 0-5 2.5 2.5 0 0 1 0 5z"/></svg>
        Harbor Cove, CA
      </li>
      <li>
        <svg viewBox="0 0 16 16" aria-hidden="true"><path d="M3.6 1 6 3.4 4.7 5.2c.9 2 2.4 3.6 4.3 4.5l1.7-1.4L13 10.7 11.3 13C6.3 12.4 2.2 8.3 1.5 3.2z"/></svg>
        949-218-4073
      </li>
    </ul>
    <ul class="contact-list contact-list--right">
      <li>
        <svg viewBox="0 0 16 16" aria-hidden="true"><path d="M1 3h14v10H1zm1.5 1.5v.4L8 8.6l5.5-3.7v-.4z"/></svg>
        marisol@tolvekmarketingconsulting.example
      </li>
      <li>
        <svg viewBox="0 0 16 16" aria-hidden="true"><circle cx="8" cy="8" r="7"/></svg>
        www.tolvekmarketingconsulting.example
      </li>
    </ul>
  </section>

  <section class="card card--back" aria-label="Card back">
    <p class="web-address">www.tolvekmarketingconsulting.example</p>
    <p class="wordmark">Tolvek Marketing<span class="wordmark__sub">Consulting</span></p>
  </section>
</main>
</body>
</html>
```